Webdesign für IT-Dienstleister
Zielgruppe
Seit 1997 bieten wir erstklassige IT-Dienstleistungen Mainz an, die darauf ausgerichtet sind, Unternehmen und Privatkunden mit kompetenter Beratung, zuverlässiger Unterstützung und modernen Technologielösungen zur Seite zu stehen.
Umfassende Computer-Serviceleistungen
Unser Computer-Service Mainz beinhaltet eine Reihe von Dienstleistungen, die darauf abzielen, die Leistungsfähigkeit Ihrer IT-Infrastruktur zu optimieren und zu erhalten. Von der Fehlerdiagnose bis hin zur Wartung bieten wir ein Rundum-Sorglos-Paket für Ihre Hardware und Software.
Professionelle Fehleranalyse und Reparatur
Optimierung von Betriebssystemen und Anwendungen
Regelmäßige Wartungsarbeiten zur Vorbeugung von Ausfällen
Ersetzen und Aufrüsten von Hardware-Komponenten
Aufgabenstellung
Ich hätte gern ein modernes Design. Ein Logo vorhanden, sollte mit eingebaut werden.
Ansonsten hätte ich gerne eine einzelne Webseite mit den Firmen Infos (und den Links zu Sozial Media) und einer extra Impressum Seite. Und wenn möglich noch ein Anfrage Formular.
Am liebsten wäre ein Format welches ich in WordPress verarbeiten werden kann.
(Logo wird noch nachgereicht)

```html
<!DOCTYPE html>
<html lang="de">
<head>
<meta charset="utf-8">
<title>Kontakt – Technikhaus Berger</title>
<link href="https://fonts.googleapis.com/css2?family=Poppins:wght@400;500;600;700&display=swap" rel="stylesheet">
<style>
:root{
  --brand:#2bb0dc;
  --navy:#1b2a55;
  --ink:#141b2d;
  --text:#3a4150;
  --muted:#8a909c;
  --line:#dfe3ea;
  --card:#f6f7f9;
  --iconbg:#e8f5fb;
  --footer:#121a2c;
  --footer-text:#b7bdca;
  --urgent:#e53935;
}
*{box-sizing:border-box;margin:0;padding:0}
html,body{width:678px;height:1200px;overflow:hidden}
body{font-family:'Poppins',sans-serif;color:var(--text);background:#fff;position:relative}
.abs{position:absolute}
svg{display:block}

.topbar{left:0;top:0;width:678px;height:17px;background:var(--brand);color:#fff;font-size:7px;display:flex;align-items:center;padding:0 42px}
.topbar .item{display:flex;align-items:center;gap:4px;margin-right:12px}
.topbar .social{margin-left:auto;display:flex;gap:9px}
.dot{width:6px;height:6px;border-radius:50%;background:#fff;opacity:.9}

.nav{left:0;top:17px;width:678px;height:31px;display:flex;align-items:center;padding:0 42px 0 48px;border-bottom:1px solid #eef0f3}
.brand{display:flex;align-items:center;gap:5px;font-size:9px;font-weight:600;color:var(--navy)}
.brand .mark{width:20px;height:20px;border-radius:50%;border:2px solid var(--brand)}
.menu{margin-left:auto;display:flex;gap:16px;font-size:8px;font-weight:500;color:var(--ink)}
.btn-head{margin-left:15px;background:var(--brand);color:#fff;font-size:8.5px;font-weight:600;border-radius:3px;width:108px;height:21px;display:flex;align-items:center;justify-content:center}

.map{left:0;top:48px;width:678px;height:180px;background:linear-gradient(100deg,#c6c8cf 0%,#c3c6cb 45%,#b9cbb3 75%,#a9c8a2 100%)}
.pin{left:328px;top:126px;width:22px;height:22px;border-radius:50%;background:var(--navy);display:flex;align-items:center;justify-content:center}

.headline{left:0;top:264px;width:678px;text-align:center}
.headline h1{font-size:18px;font-weight:700;color:var(--ink)}
.headline p{font-size:10px;line-height:13.5px;margin-top:6px;color:var(--text)}

.info{left:42px;top:350px;width:280px}
.info h2{font-size:12px;font-weight:600;color:var(--ink)}
.info-item{position:absolute;left:0;display:flex;gap:11px}
.icon-box{width:27px;height:27px;border-radius:5px;background:var(--iconbg);display:flex;align-items:center;justify-content:center;flex:none}
.info-item h3{font-size:9px;font-weight:600;color:var(--ink);margin-bottom:4px}
.info-item p{font-size:8px;line-height:12.5px}
.info-item .hl{color:var(--brand);font-size:7.5px;font-weight:500}

.form-card{left:354px;top:350px;width:282px;height:450px;background:var(--card);border-radius:8px;padding:15px}
.form-card h2{font-size:12px;font-weight:600;color:var(--ink)}
.form-card .lead{font-size:8px;line-height:11.5px;margin-top:13px}
.label{position:absolute;font-size:7px;font-weight:500;color:var(--ink)}
.field{position:absolute;height:21px;background:#fff;border:1px solid var(--line);border-radius:5px;font-size:6.8px;color:var(--muted);padding:0 7px;display:flex;align-items:center;white-space:nowrap;overflow:hidden}
.field.select{color:var(--ink);justify-content:space-between}
.radios{position:absolute;left:15px;top:233px;display:flex;gap:8px;font-size:7.5px;color:var(--ink)}
.radio{display:flex;align-items:center;gap:3px}
.radio .r{width:9px;height:9px;border-radius:50%;border:1px solid #b8bec8;background:#fff}
.radio .r.on{border:1.5px solid var(--navy);box-shadow:inset 0 0 0 1.5px #fff;background:var(--navy)}
.radio.urgent{color:var(--urgent)}
.radio.urgent .r{border-color:var(--urgent)}
.check{position:absolute;left:15px;display:flex;gap:6px;font-size:7px;line-height:9.5px;color:var(--ink);width:250px}
.check .box{width:9px;height:9px;border:1px solid #b8bec8;border-radius:50%;flex:none;margin-top:1px;background:#fff}
.check b{font-weight:600;color:var(--navy)}
.btn-send{position:absolute;left:15px;top:409px;width:167px;height:24px;background:var(--brand);color:#fff;border-radius:3px;font-size:8.5px;font-weight:600;display:flex;align-items:center;justify-content:center;gap:5px}
.btn-reset{position:absolute;left:190px;top:409px;width:76px;height:24px;border:1px solid #c7ccd4;border-radius:3px;background:#fff;color:var(--ink);font-size:8.5px;font-weight:600;display:flex;align-items:center;justify-content:center}

.cta{left:0;top:837px;width:678px;height:147px;background:radial-gradient(circle at 30% 40%,#26407a 0%,#1c2e5e 55%,#172650 100%);text-align:center;color:#fff}
.cta h2{font-size:15px;font-weight:700;margin-top:31px}
.cta p{font-size:10px;margin-top:9px;color:#e6ebf5}
.cta .btns{display:flex;gap:8px;justify-content:center;margin-top:15px}
.cta .b{height:28px;border-radius:3px;font-size:8px;font-weight:600;display:flex;align-items:center;justify-content:center;gap:5px}
.cta .b1{width:134px;background:var(--brand)}
.cta .b2{width:126px;border:1.2px solid #fff}

.footer{left:0;top:984px;width:678px;height:216px;background:var(--footer);color:var(--footer-text)}
.footer .brand{position:absolute;left:42px;top:30px;color:#fff}
.footer .about{position:absolute;left:42px;top:64px;font-size:8px;line-height:11.5px;width:180px}
.footer .socials{position:absolute;left:42px;top:99px;display:flex;gap:8px}
.footer .socials span{width:15px;height:15px;border-radius:50%;background:#222b3e}
.col{position:absolute;top:32px;font-size:8px}
.col h4{color:#fff;font-size:9px;font-weight:600;margin-bottom:14px}
.col .row{display:flex;gap:8px;margin-bottom:8px;line-height:11.5px}
.col .link{margin-bottom:7.5px}
.footer .rule{position:absolute;left:42px;top:158px;width:594px;height:1px;background:#232c40}
.footer .copy{position:absolute;left:0;top:174px;width:678px;text-align:center;font-size:8px}
</style>
</head>
<body>

<div class="abs topbar">
  <div class="item"><svg width="6" height="6" viewBox="0 0 24 24" fill="none" stroke="#fff" stroke-width="2.5"><path d="M22 16.9v3a2 2 0 0 1-2.2 2A19.8 19.8 0 0 1 2.1 4.2 2 2 0 0 1 4.1 2h3a2 2 0 0 1 2 1.7l.5 3a2 2 0 0 1-.6 1.8L7.6 9.9a16 16 0 0 0 6.5 6.5l1.4-1.4a2 2 0 0 1 1.8-.6l3 .5a2 2 0 0 1 1.7 2z"/></svg>+49 6131 480210</div>
  <div class="item"><svg width="6" height="6" viewBox="0 0 24 24" fill="none" stroke="#fff" stroke-width="2.5"><rect x="2" y="4" width="20" height="16" rx="2"/><path d="m22 6-10 7L2 6"/></svg>info@berger-it.example</div>
  <div class="social"><span class="dot"></span><span class="dot"></span><span class="dot"></span></div>
</div>

<header class="abs nav">
  <div class="brand"><span class="mark"></span>Technikhaus Berger</div>
  <nav class="menu"><span>Home</span><span>Services</span><span>Verkauf</span><span>Kontakt</span></nav>
  <div class="btn-head">Service anfordern</div>
</header>

<div class="abs map" role="img" aria-label="Stadtplan mit Standort des Geschäfts"></div>
<div class="abs pin"><svg width="8" height="8" viewBox="0 0 24 24" fill="#fff"><path d="M12 2a7 7 0 0 0-7 7c0 5 7 13 7 13s7-8 7-13a7 7 0 0 0-7-7zm0 9.5A2.5 2.5 0 1 1 12 6.5a2.5 2.5 0 0 1 0 5z"/></svg></div>

<section class="abs headline">
  <h1>Kontakt</h1>
  <p>Haben Sie Fragen oder benötigen Sie Unterstützung? Wir sind für Sie da und<br>freuen uns auf Ihre Nachricht!</p>
</section>

<section class="abs info">
  <h2>Kontaktinformationen</h2>
  <div class="info-item" style="top:31px">
    <div class="icon-box"><svg width="9" height="9" viewBox="0 0 24 24" fill="none" stroke="#2bb0dc" stroke-width="2"><path d="M12 22s7-7 7-12a7 7 0 0 0-14 0c0 5 7 12 7 12z"/><circle cx="12" cy="10" r="2.5"/></svg></div>
    <div><h3>Geschäftsadresse</h3><p>Lindenweg 48<br>55118 Mainz<br>Deutschland</p></div>
  </div>
  <div class="info-item" style="top:100px">
    <div class="icon-box"><svg width="9" height="9" viewBox="0 0 24 24" fill="none" stroke="#2bb0dc" stroke-width="2"><path d="M22 16.9v3a2 2 0 0 1-2.2 2A19.8 19.8 0 0 1 2.1 4.2 2 2 0 0 1 4.1 2h3a2 2 0 0 1 2 1.7l.5 3a2 2 0 0 1-.6 1.8L7.6 9.9a16 16 0 0 0 6.5 6.5l1.4-1.4a2 2 0 0 1 1.8-.6l3 .5a2 2 0 0 1 1.7 2z"/></svg></div>
    <div><h3>Telefon &amp; Fax</h3><p>Telefon: +49 6131 480210<br>Fax: +49 6131 480211<br>Notfall-Hotline: +49 6131 480212</p></div>
  </div>
  <div class="info-item" style="top:170px">
    <div class="icon-box"><svg width="9" height="9" viewBox="0 0 24 24" fill="none" stroke="#2bb0dc" stroke-width="2"><rect x="2" y="4" width="20" height="16" rx="2"/><path d="m22 6-10 7L2 6"/></svg></div>
    <div><h3>E-Mail Adressen</h3><p>Allgemein: info@berger-it.example<br>Support: support@berger-it.example<br>Verkauf: verkauf@berger-it.example</p></div>
  </div>
  <div class="info-item" style="top:239px">
    <div class="icon-box"><svg width="9" height="9" viewBox="0 0 24 24" fill="none" stroke="#2bb0dc" stroke-width="2"><circle cx="12" cy="12" r="9"/><path d="M12 7v5l3 2"/></svg></div>
    <div><h3>Öffnungszeiten</h3><p>Montag - Freitag: 08:00 - 18:00 Uhr<br>Samstag: 09:00 - 14:00 Uhr<br>Sonntag: Geschlossen<br><span class="hl">24/7 Notfall-Service verfügbar</span></p></div>
  </div>
  <div class="info-item" style="top:321px">
    <div class="icon-box"><svg width="9" height="9" viewBox="0 0 24 24" fill="none" stroke="#2bb0dc" stroke-width="2"><path d="M5 17h14v-5l-2-5H7l-2 5z"/><path d="M5 12h14"/><circle cx="8" cy="15" r=".5"/><circle cx="16" cy="15" r=".5"/></svg></div>
  </div>
</section>

<section class="abs form-card">
  <h2>Nachricht senden</h2>
  <p class="lead">Senden Sie uns eine Nachricht und wir melden uns<br>schnellstmöglich bei Ihnen zurück.</p>

  <span class="label" style="left:15px;top:80px">Vor- und Nachname *</span>
  <span class="label" style="left:147px;top:80px">E-Mail Adresse *</span>
  <div class="field" style="left:15px;top:94px;width:120px">Max Mustermann</div>
  <div class="field" style="left:147px;top:94px;width:120px">max.mustermann@email.de</div>

  <span class="label" style="left:15px;top:127px">Telefonnummer</span>
  <span class="label" style="left:147px;top:127px">Unternehmen</span>
  <div class="field" style="left:15px;top:140px;width:120px">+49 123 456789</div>
  <div class="field" style="left:147px;top:140px;width:120px">Firma GmbH</div>

  <span class="label" style="left:15px;top:173px">Betreff *</span>
  <div class="field select" style="left:15px;top:187px;width:252px">Bitte wählen Sie einen Betreff<svg width="6" height="6" viewBox="0 0 24 24" fill="none" stroke="#555" stroke-width="2.5"><path d="m6 9 6 6 6-6"/></svg></div>

  <span class="label" style="left:15px;top:220px">Priorität</span>
  <div class="radios">
    <span class="radio"><span class="r on"></span>Niedrig</span>
    <span class="radio"><span class="r"></span>Normal</span>
    <span class="radio"><span class="r"></span>Hoch</span>
    <span class="radio urgent"><span class="r"></span>Dringend</span>
  </div>

  <span class="label" style="left:15px;top:255px">Ihre Nachricht *</span>
  <div class="field" style="left:15px;top:268px;width:252px;height:69px;align-items:flex-start;padding-top:7px">Beschreiben Sie bitte Ihr Anliegen oder Problem...</div>

  <div class="check" style="top:356px"><span class="box"></span><span>Ich möchte gelegentlich Informationen über neue Services und Angebote erhalten.</span></div>
  <div class="check" style="top:383px"><span class="box"></span><span>Ich stimme der Verarbeitung meiner Daten gemäß der <b>Datenschutzerklärung</b> zu. *</span></div>

  <div class="btn-send"><svg width="7" height="7" viewBox="0 0 24 24" fill="none" stroke="#fff" stroke-width="2.5"><path d="M22 2 11 13"/><path d="M22 2 15 22l-4-9-9-4z"/></svg>Nachricht senden</div>
  <div class="btn-reset">Zurücksetzen</div>
</section>

<section class="abs cta" role="img" aria-label="Dunkelblauer Hintergrund mit Netzwerk-Motiv">
  <h2>Brauchen Sie sofortige Hilfe?</h2>
  <p>Unser 24/7 Notfall-Service steht Ihnen bei kritischen IT-Problemen zur Verfügung.</p>
  <div class="btns">
    <div class="b b1"><svg width="7" height="7" viewBox="0 0 24 24" fill="none" stroke="#fff" stroke-width="2.5"><path d="M22 16.9v3a2 2 0 0 1-2.2 2A19.8 19.8 0 0 1 2.1 4.2 2 2 0 0 1 4.1 2h3a2 2 0 0 1 2 1.7l.5 3a2 2 0 0 1-.6 1.8L7.6 9.9a16 16 0 0 0 6.5 6.5l1.4-1.4a2 2 0 0 1 1.8-.6l3 .5a2 2 0 0 1 1.7 2z"/></svg>Notfall-Hotline anrufen</div>
    <div class="b b2"><svg width="7" height="7" viewBox="0 0 24 24" fill="none" stroke="#fff" stroke-width="2.5"><rect x="2" y="4" width="20" height="16" rx="2"/><path d="m22 6-10 7L2 6"/></svg>Sofort E-Mail senden</div>
  </div>
</section>

<footer class="abs footer">
  <div class="brand"><span class="mark"></span>Technikhaus Berger</div>
  <p class="about">Seit 1997 Ihr vertrauensvoller Partner für professionelle IT-Dienstleistungen in Mainz.</p>
  <div class="socials"><span></span><span></span><span></span></div>

  <div class="col" style="left:245px">
    <h4>Kontakt</h4>
    <div class="row"><svg width="6" height="6" viewBox="0 0 24 24" fill="none" stroke="#b7bdca" stroke-width="2" style="margin-top:3px"><path d="M12 22s7-7 7-12a7 7 0 0 0-14 0c0 5 7 12 7 12z"/></svg><span>Lindenweg 48<br>55118 Mainz, Deutschland</span></div>
    <div class="row"><svg width="6" height="6" viewBox="0 0 24 24" fill="none" stroke="#b7bdca" stroke-width="2" style="margin-top:3px"><path d="M22 16.9v3a2 2 0 0 1-2.2 2A19.8 19.8 0 0 1 2.1 4.2 2 2 0 0 1 4.1 2h3a2 2 0 0 1 2 1.7l.5 3a2 2 0 0 1-.6 1.8L7.6 9.9a16 16 0 0 0 6.5 6.5l1.4-1.4a2 2 0 0 1 1.8-.6l3 .5a2 2 0 0 1 1.7 2z"/></svg><span>+49 6131 480210</span></div>
    <div class="row"><svg width="6" height="6" viewBox="0 0 24 24" fill="none" stroke="#b7bdca" stroke-width="2" style="margin-top:3px"><rect x="2" y="4" width="20" height="16" rx="2"/><path d="m22 6-10 7L2 6"/></svg><span>info@berger-it.example</span></div>
  </div>

  <div class="col" style="left:448px">
    <h4>Wichtige Links</h4>
    <div class="link">Home</div>
    <div class="link">Services</div>
    <div class="link">Kontakt</div>
    <div class="link">Impressum</div>
    <div class="link">Datenschutz</div>
  </div>

  <div class="rule"></div>
  <p class="copy">© 2025 berger-it.example – Technikhaus Berger. Alle Rechte vorbehalten.</p>
</footer>

</body>
</html>
```